Brookhaven Sound Vision Guard LLC

Need help designing a web page for an alarm company. I want to promote my business.

Target Market(s)

Residential and commercial clients

Industry/Entity Type

Security Service

Coding

Coded - Design and coding required

Number of Pages Required

2 page

Font styles to use
Sans Serif

Requirements
Must have
• I would llike my logo displayed on the page. I would like my slogan displayed as well
´´A GREAT PLACE FOR YOUR SECURITY NEEDS´´
We are licensed and insured
Company phone number 555-204-7163
Company hours: Monday-Friday 8am-5pm Company address: P.O. Box 412 Crosby, TX 77500 over 25 years experience
Email info. Brookhavensvg@mailbox.example
Company license #K41862259
Fire license# TDM-5817026
PLH-7064183
We offer alarm monitoring,security cameras, access control,gate openers, home theater systems, covert camera installations, FIre alarm installation and monitoring
Nice to have
• We offer security at competitive prices.
Get customer information for a free quote similar to vexo website.
Should not have
• No prices listed on website

```html
<!DOCTYPE html>
<html lang="en">
<head>
<meta charset="utf-8">
<title>Brookhaven Sound Vision Guard</title>
<link href="https://fonts.googleapis.com/css2?family=Poppins:ital,wght@0,400;0,500;0,600;1,600&display=swap" rel="stylesheet">
<style>
:root{
  --red:#e8453c;
  --white:#ffffff;
  --ink:#2b2b2b;
  --muted:#8a8a8a;
  --bar:#e6e6e6;
  --hero-top:#1b1f4d;
  --hero-mid:#5a3f78;
  --hero-low:#3a2432;
  --dark-a:#22201f;
  --dark-b:#2f3a3c;
  --footer-line:#d9d9d9;
}
*{margin:0;padding:0;box-sizing:border-box}
html,body{width:899px;height:1200px;overflow:hidden;background:var(--white)}
body{position:relative;font-family:'Poppins',sans-serif;color:var(--ink)}
.abs{position:absolute}

.hero{left:0;top:0;width:899px;height:511px}
.hero-photo{position:absolute;inset:0;background:
  linear-gradient(180deg,var(--hero-top) 0%,var(--hero-mid) 40%,#6a4762 55%,var(--hero-low) 100%)}
.hero-photo::after{content:"";position:absolute;inset:0;background:
  radial-gradient(ellipse at 75% 15%,rgba(214,120,100,.45),transparent 55%),
  radial-gradient(ellipse at 35% 85%,rgba(230,90,40,.35),transparent 60%)}

.brand{display:flex;align-items:center;gap:5px;font-weight:600;letter-spacing:.02em}
.brand-dot{width:10px;height:10px;border-radius:50%;background:var(--red);flex:none}
.brand--header{left:130px;top:20px;font-size:12px;color:var(--white)}

.nav{top:20px;left:0;font-size:10px;font-weight:500;color:var(--white)}
.nav a{position:absolute;color:var(--white);text-decoration:none;white-space:nowrap}
.nav a.is-active{border-bottom:1px solid var(--white);padding-bottom:1px}

.slogan{left:130px;top:174px;font-size:24px;font-weight:600;font-style:italic;line-height:36px;color:var(--white);letter-spacing:.01em}
.hero-sub{left:130px;top:242px;font-size:12px;line-height:18px;color:var(--white)}
.btn{display:inline-flex;align-items:center;justify-content:center;background:var(--red);color:var(--white);border-radius:3px;text-decoration:none}
.btn--hero{left:130px;top:290px;width:85px;height:29px;font-size:12.5px}
.contact{left:130px;top:435px;font-size:12.5px;line-height:19px;color:rgba(255,255,255,.8)}
.load-more{left:407px;top:454px;font-size:16px;font-weight:600;color:var(--white);display:flex;align-items:center;gap:6px}

.welcome{left:0;width:899px;top:545px;text-align:center;font-size:9.5px;color:var(--muted)}
.brand--main{left:0;width:899px;top:606px;justify-content:center;font-size:22px;color:var(--ink);gap:8px}
.brand--main .brand-dot{width:22px;height:22px}
.about{left:243px;width:413px;top:678px;text-align:center;font-size:10px;line-height:14px;color:#4a4a4a}
.btn--about{left:418px;top:722px;width:63px;height:22px;font-size:9.5px}

.bar{background:var(--bar);width:13.5px;bottom:379px}

.license{left:0;top:821px;width:899px;height:269px}
.license-photo{position:absolute;inset:0;background:
  linear-gradient(90deg,var(--dark-a) 0%,#2a2624 50%,#4a4d4c 51%,#3a4244 80%,var(--dark-b) 100%)}
.license-photo::after{content:"";position:absolute;left:0;right:0;bottom:0;height:110px;background:linear-gradient(180deg,transparent,rgba(20,40,44,.7))}
.license-title{left:66px;top:834px;font-size:15px;font-weight:600;color:var(--white)}
.license-list{left:66px;top:876px;font-size:12.5px;line-height:18px;color:var(--white)}
.btn--license{left:66px;top:952px;width:64px;height:22px;font-size:9.5px}

.footer{left:0;top:1090px;width:899px;height:110px;border:1px solid var(--footer-line);border-top:none}
.brand--footer{left:130px;top:1138px;font-size:12px;color:var(--ink)}
.social{top:1134px;width:24px;height:24px;border-radius:50%;border:1px solid #7a7a7a}
</style>
</head>
<body>

<section class="abs hero">
  <div class="hero-photo" role="img" aria-label="Night city skyline at dusk with a security camera on a pole"></div>
</section>

<div class="abs brand brand--header"><span class="brand-dot"></span>Brookhaven</div>

<nav class="abs nav">
  <a class="is-active" style="left:463px">Home</a>
  <a style="left:519px">Category</a>
  <a style="left:592px">License</a>
  <a style="left:655px">About me</a>
  <a style="left:730px">Contact</a>
</nav>

<h1 class="abs slogan">´´A GREAT PLACE FOR<br>SECURITY NEEDS´´</h1>
<p class="abs hero-sub">Lets get buy first one and<br>get it discount - Free</p>
<a class="abs btn btn--hero">Read More</a>

<p class="abs contact">555-204-7163<br>Brookhavensvg@mailbox.example</p>

<div class="abs load-more">Load More
  <svg width="14" height="8" viewBox="0 0 14 8"><path d="M1 1l6 6 6-6" fill="none" stroke="#fff" stroke-width="1.3"/></svg>
</div>

<div class="abs bar" style="left:0;top:707px"></div>
<div class="abs bar" style="left:24px;top:674px"></div>
<div class="abs bar" style="left:49px;top:732px"></div>
<div class="abs bar" style="left:73px;top:712px"></div>
<div class="abs bar" style="left:98px;top:763px"></div>
<div class="abs bar" style="left:788px;top:763px"></div>
<div class="abs bar" style="left:812px;top:712px"></div>
<div class="abs bar" style="left:837px;top:732px"></div>
<div class="abs bar" style="left:861px;top:674px"></div>
<div class="abs bar" style="left:885px;top:707px"></div>

<p class="abs welcome">Welcome to</p>
<div class="abs brand brand--main"><span class="brand-dot"></span>Brookhaven Sound Vision Guard</div>
<p class="abs about">We offer alarm monitoring,security cameras, access control,gate openers, home theater systems, covert camera installations, FIre alarm installation and monitoring</p>
<a class="abs btn btn--about">Read More</a>

<section class="abs license">
  <div class="license-photo" role="img" aria-label="Security cameras and alarm siren mounted on a dark brick and metal wall"></div>
</section>
<h2 class="abs license-title">We have license and Insured</h2>
<p class="abs license-list">Company license #K41862259<br>Fire license# TDM-5817026<br>PLH-7064183</p>
<a class="abs btn btn--license">Read More</a>

<footer class="abs footer"></footer>
<div class="abs brand brand--footer"><span class="brand-dot"></span>Brookhaven</div>
<span class="abs social" style="left:623px" aria-label="Social link"></span>
<span class="abs social" style="left:670px" aria-label="Social link"></span>
<span class="abs social" style="left:717px" aria-label="Social link"></span>
<span class="abs social" style="left:764px" aria-label="Social link"></span>

</body>
</html>
```